Banner Ad Design for Coinharbor.com

We save people money--we have partnered with [login to view URL] to provide instant savings that will put a lot of money back into people's pockets.
Our target market is everyone who likes to save money--or concerned about money. We are located in Utah USA

```html
<!DOCTYPE html>
<html lang="en">
<head>
<meta charset="utf-8">
<title>Coinharbor.com Banner</title>
<link rel="stylesheet" href="https://fonts.googleapis.com/css2?family=Jost:wght@400;500;700&display=swap">
<style>
  :root {
    --blue-deep: #1636a6;
    --blue-mid: #2653cc;
    --blue-light: #3a72e6;
    --white: #ffffff;
    --cash-cream: #e8dcc0;
    --cash-green: #9fae8c;
    --cash-band: #c8a777;
  }
  html, body {
    margin: 0;
    padding: 0;
    width: 1200px;
    height: 840px;
    overflow: hidden;
    background: var(--blue-deep);
  }
  .banner {
    position: relative;
    width: 1200px;
    height: 840px;
    overflow: hidden;
    font-family: "Jost", "Century Gothic", sans-serif;
    color: var(--white);
    background: radial-gradient(ellipse at 50% 45%, var(--blue-light) 0%, var(--blue-mid) 45%, var(--blue-deep) 100%);
  }
  .banner * { position: absolute; margin: 0; }
  .headline-lead {
    top: 22px; left: 0; width: 1200px;
    text-align: center;
    font-size: 54px; font-weight: 400;
    line-height: 1;
  }
  .headline-main {
    top: 108px; left: 0; width: 1200px;
    text-align: center;
    font-size: 74px; font-weight: 700;
    line-height: 1;
  }
  .cash-stack {
    left: 228px; top: 226px;
    width: 430px; height: 376px;
    border-radius: 10px;
    background: linear-gradient(160deg, var(--cash-cream) 0%, var(--cash-green) 55%, var(--cash-band) 100%);
  }
  .find-out {
    left: 690px; top: 234px;
    font-size: 58px; font-weight: 400;
    line-height: 1;
  }
  .free-word {
    left: 752px; top: 330px;
    font-size: 170px; font-weight: 500;
    line-height: 1; letter-spacing: 2px;
  }
  .savings-note {
    right: 72px; top: 536px;
    text-align: right;
    font-size: 36px; font-weight: 400;
    line-height: 48px;
  }
  .tagline {
    left: 30px; top: 670px;
    font-size: 39px; font-weight: 400;
    line-height: 1;
  }
  .cta {
    right: 136px; top: 744px;
    display: flex; align-items: baseline;
    line-height: 1;
    white-space: nowrap;
  }
  .cta-lead { position: static; font-size: 44px; font-weight: 400; margin-right: 16px; }
  .cta-site { position: static; font-size: 60px; font-weight: 700; }
  .cta-arrow {
    right: 76px; top: 748px;
    width: 48px; height: 54px;
  }
</style>
</head>
<body>
  <main class="banner">
    <p class="headline-lead">What Could You do With</p>
    <h1 class="headline-main">an EXTRA $250/month?</h1>
    <div class="cash-stack" role="img" aria-label="Two stacks of banded dollar bills"></div>
    <p class="find-out">Find Out Today!</p>
    <p class="free-word">Free</p>
    <p class="savings-note">Put up $250 a month back<br>into your pocket ...Instantly!</p>
    <p class="tagline">Get Smart with your Money</p>
    <p class="cta"><span class="cta-lead">It’s free at</span><span class="cta-site">Coinharbor.com</span></p>
    <svg class="cta-arrow" viewBox="0 0 48 54" aria-hidden="true">
      <rect x="2" y="2" width="44" height="50" rx="6" fill="none" stroke="#ffffff" stroke-width="4"/>
      <path d="M17 14 L34 27 L17 40 Z" fill="#ffffff"/>
    </svg>
  </main>
</body>
</html>
```